Flyer Design Project for our Parenting Psychologists at the Wellmind Counselling Centre

At the Wellmind Counselling Centre we have expert Parenting Psychologists.

Parenting Psychologists provide practical, step by step assistance to parents who are struggling with their children's behavioural and emotional problems.

We need a DL size brochure that will be appealing to parents. The brochure will be on show in schools, kindergartens and GP clinics.

In terms of style it will be in line with our website and stationery that I will attach.

www.wellmindcounsellingcentre.com.au

Hi Everyone,
Thanks for putting forward your proposals, there are a couple there that I am very interested in. I am looking to see if there is a way that I can change my brief to guaranteed as I am definitely going to be using one of the designs for sure.
I have emailed ArtForge and as soon as I get an answer I will change it if I can.
If anyone out there already knows the answer please let me know :-)
Thanks,
Marcie.

Hi Again,

I worked it out myself!!

I have now changed this to a committed project.

Kind regards,
Marcie.

Reason: I have 46 designs now and need more time to work out which is best!

Target Market(s)

The target will be educated professional parents motivated to get professional help. And doctors and teachers who will pass on the brochures 2 parents

Industry/Entity Type

Health

Requirements
Must have
• I want one DL size brochure. Back and front.

We need text (below) and our contact details. Our logo.

6352 1840
Suite 1, 2087 Tamworth Rd, Tamworth North 3118

Text:
Parents want the best for their kids. They want kids that are happy, healthy and well behaved.

So why is it so hard? Parents of toddlers, primary schoolers and teenagers alike say that they are frustrated by constant nagging, bribing and yelling, they don't know what to try next. Some parents worry that their children are unhappy. Struggling at school, not making friends or coping with bigger problems.

The good news is that getting your children to behave more co-operatively doesn't need to be difficult or mysterious. We all know that kids don't come with manuals, but there are skills every parent can learn to make parenting easier. In a few sessions with a Parenting Psychologist, you will receive step by step guidance in how to talk to your children in a way that will be much more effective getting them to behave in a respectful and co-operative way around the home and in public. You will learn how to help your child cope with problems they are going through. They can help you reconnect with your kids so you can enjoy being a parent again.

Nice to have
• Themes consistent with our website
and letterhead, business cards. I will attach these.
Should not have
• I don't want it to look too cluttered so if the text I have provided up above looks too crowded then I will edit it.

```html
<!DOCTYPE html>
<html lang="en">
<head>
<meta charset="utf-8">
<title>Wellmind Counselling Centre – Parenting Brochure</title>
<link href="https://fonts.googleapis.com/css2?family=Lato:wght@300;400;700&display=swap" rel="stylesheet">
<style>
  :root {
    --bg: #eceeef;
    --paper: #ffffff;
    --mist: #e1e5e6;
    --teal: #6fb5b8;
    --teal-dark: #4f9ea3;
    --slate: #7f97a8;
    --slate-dark: #6c8596;
    --steel: #8aa6b6;
    --lavender: #c6cbe8;
    --ink: #3f4347;
    --ink-soft: #5c6166;
    --rule: #dde1e3;
  }
  * { box-sizing: border-box; margin: 0; padding: 0; }
  html, body { width: 1200px; height: 795px; overflow: hidden; }
  body {
    background: var(--bg);
    font-family: "Lato", sans-serif;
    color: var(--ink);
    position: relative;
  }
  .panel {
    position: absolute;
    top: 46px;
    width: 334px;
    height: 704px;
    background: var(--paper);
    box-shadow: 0 6px 18px rgba(0,0,0,0.12);
    display: flex;
    flex-direction: column;
    overflow: hidden;
  }
  .panel--front { left: 248px; }
  .panel--back { left: 618px; }

  .stripe { display: flex; height: 9px; flex: none; }
  .stripe span { flex: 1; }
  .stripe .s1 { background: var(--slate); flex: 1.4; }
  .stripe .s2 { background: var(--teal); flex: 2.2; }
  .stripe .s3 { background: var(--slate-dark); flex: 1; }
  .stripe .s4 { background: var(--teal); flex: 1.6; }
  .stripe .s5 { background: #a9c9cc; flex: 0.8; }

  /* front */
  .front-head {
    background: var(--mist);
    height: 232px;
    display: flex;
    align-items: center;
    padding: 0 30px;
  }
  .brand-name {
    font-weight: 400;
    font-size: 24px;
    line-height: 1.25;
    color: var(--teal-dark);
  }
  .stripe--mid { height: 8px; }
  .front-photo {
    height: 212px;
    background: linear-gradient(135deg, #a7c27e 0%, #6e9a4f 45%, #8aa9c4 100%);
  }
  .front-body {
    flex: 1;
    background: var(--mist);
    padding: 26px 22px;
    display: flex;
  }
  .contact {
    background: var(--lavender);
    border-radius: 14px;
    width: 100%;
    height: 150px;
    padding: 28px 24px;
    font-size: 14px;
    line-height: 1.5;
    font-style: normal;
    color: var(--ink);
  }
  .contact strong { font-weight: 700; margin-right: 8px; }

  /* back */
  .back-lead {
    padding: 26px 26px 16px;
    font-size: 17px;
    line-height: 1.25;
    color: var(--teal-dark);
    border-bottom: 1px solid var(--rule);
  }
  .back-copy { padding: 22px 26px 0; flex: 1; }
  .back-copy h2 {
    font-weight: 700;
    font-size: 16px;
    text-transform: uppercase;
    color: var(--ink);
    margin-bottom: 10px;
  }
  .back-copy p {
    font-size: 11.6px;
    line-height: 1.5;
    color: var(--ink-soft);
  }
  .back-copy .divider { height: 1px; background: var(--rule); margin: 16px 0; }
  .back-foot {
    background: var(--steel);
    height: 104px;
    flex: none;
    display: flex;
    flex-direction: column;
  }
  .back-foot .url {
    flex: 1;
    display: flex;
    align-items: center;
    justify-content: center;
    color: #ffffff;
    font-size: 14.5px;
  }
</style>
</head>
<body>
  <section class="panel panel--front">
    <div class="stripe"><span class="s1"></span><span class="s2"></span><span class="s3"></span><span class="s4"></span><span class="s5"></span></div>
    <header class="front-head">
      <div class="brand-name">Wellmind Counselling Centre</div>
    </header>
    <div class="stripe stripe--mid"><span class="s2"></span><span class="s1"></span><span class="s4"></span><span class="s5"></span></div>
    <div class="front-photo" role="img" aria-label="Photograph of a young child playing outdoors on a sunny lawn"></div>
    <div class="stripe stripe--mid"><span class="s4"></span><span class="s3"></span><span class="s2"></span></div>
    <div class="front-body">
      <address class="contact">
        <div><strong>tel</strong>6352 1840</div>
        <div>Suite 1, 2087 Tamworth Rd,</div>
        <div>Tamworth North 3118</div>
        <div>www.wellmindcounsellingcentre.com.au</div>
      </address>
    </div>
    <div class="stripe"><span class="s3"></span><span class="s2"></span><span class="s1"></span><span class="s4"></span></div>
  </section>

  <section class="panel panel--back">
    <div class="stripe"><span class="s1"></span><span class="s2"></span><span class="s3"></span><span class="s4"></span><span class="s5"></span></div>
    <p class="back-lead">Parents want the best for their kids. They want kids that are happy, healthy and well behaved.</p>
    <div class="back-copy">
      <h2>So why is it so hard?</h2>
      <p>Parents of toddlers, primary schoolers and teenagers alike say that they are frustrated by constant nagging, bribing and yelling, they don't know what to try next. Some parents worry that their children are unhappy. Struggling at school, not making friends or coping with bigger problems.</p>
      <div class="divider"></div>
      <p>The good news is that getting your children to behave more co-operatively doesn't need to be difficult or mysterious. We all know that kids don't come with manuals, but there are skills every parent can learn to make parenting easier. In a few sessions with a Parenting Psychologist, you will receive step by step guidance in how to talk to your children in a way that will be much more effective getting them to behave in a respectful and co-operative way around the home and in public. You will learn how to help your child cope with problems they are going through. They can help you reconnect with your kids so you can enjoy being a parent again.</p>
    </div>
    <footer class="back-foot">
      <div class="stripe"><span class="s2"></span><span class="s1"></span><span class="s4"></span><span class="s3"></span></div>
      <div class="url">www.wellmindcounsellingcentre.com.au</div>
    </footer>
  </section>
</body>
</html>
```